Contemporary Elegant Business Card Design for an International Trade Company in the Wine Industry

We need a new business card design for an international trade company in the wine and winemaking industry. The overall feel of the card should be contemporary, upscale, luxurious and elegant. It should communicate confidence and professionalism. The colors should complementary to our logo design (burgundy, gold, and black).
Inspiration: rich velvet tapestry
The card should include the following information:
Business: Brovenna Trading/Shipping, LLC.
Name: Marcus T. Hollenbrand
Title: CEO
Email: mark@brovennatrading.example
Phone: 555-294-6172
www.brovennatrading.example
Updates
Project Deadline Extended
Reason: We'd like the designers that we requested some additional designs from to still submit designs. Thank you!
Industry/Entity Type
Business
Contact Information for Business Card
Title: CEO
Phone: 555-294-6172
www.brovennatrading.example
Look and feel

```html
<!DOCTYPE html>
<html lang="en">
<head>
<meta charset="utf-8">
<title>Brovenna Trading/Shipping — Business Card</title>
<link href="https://fonts.googleapis.com/css2?family=Open+Sans:wght@400;600&display=swap" rel="stylesheet">
<style>
  :root {
    --stage: #e9e4dc;
    --velvet-light: #7a2a17;
    --velvet-mid: #5a1c10;
    --velvet-dark: #2a0d07;
    --gold: #e8b452;
    --gold-deep: #b9802f;
    --gold-band-end: #c58a3a;
    --ink-light: #fdf3e2;
    --muted: #c49a7e;
  }
  * { box-sizing: border-box; margin: 0; padding: 0; }
  html, body { width: 1200px; height: 900px; overflow: hidden; }
  body {
    background: var(--stage);
    font-family: "Open Sans", Arial, sans-serif;
    position: relative;
  }
  .card {
    position: absolute;
    width: 600px;
    height: 356px;
    overflow: hidden;
    box-shadow: 0 10px 28px rgba(40, 20, 10, 0.28);
    background:
      radial-gradient(ellipse at 70% 20%, rgba(150, 60, 30, 0.55), transparent 55%),
      radial-gradient(ellipse at 20% 85%, rgba(20, 5, 3, 0.7), transparent 60%),
      radial-gradient(ellipse at 90% 90%, rgba(30, 8, 4, 0.5), transparent 50%),
      linear-gradient(135deg, var(--velvet-mid), var(--velvet-light) 45%, var(--velvet-mid) 75%, var(--velvet-dark));
  }
  .card--front { left: 90px; top: 100px; }
  .card--back { left: 510px; top: 484px; }

  /* Brand lockup */
  .brand {
    position: absolute;
    left: 38px;
    top: 38px;
    display: flex;
    flex-direction: column;
    align-items: flex-start;
    gap: 12px;
  }
  .brand-square {
    width: 130px;
    height: 130px;
    background: var(--gold);
  }
  .brand-name {
    font-weight: 600;
    font-size: 22px;
    letter-spacing: 1px;
    color: var(--gold);
    text-transform: uppercase;
    line-height: 1;
  }

  /* Name band */
  .name-band {
    position: absolute;
    left: 236px;
    right: 0;
    top: 226px;
    height: 72px;
    background: linear-gradient(90deg, rgba(185, 128, 47, 0), var(--gold-deep) 45%, var(--gold-band-end));
    display: flex;
    flex-direction: column;
    align-items: flex-end;
    justify-content: center;
    padding-right: 66px;
  }
  .person-name {
    font-size: 26px;
    font-weight: 400;
    color: var(--ink-light);
    line-height: 1.15;
  }
  .person-title {
    font-size: 14px;
    color: var(--ink-light);
    line-height: 1.2;
  }

  /* Contact line */
  .contact-line {
    position: absolute;
    left: 40px;
    right: 40px;
    top: 318px;
    display: flex;
    justify-content: center;
    gap: 10px;
    font-size: 11px;
    color: var(--muted);
    white-space: nowrap;
  }

  /* Back */
  .back-brand {
    position: absolute;
    left: 0;
    right: 0;
    top: 40px;
    display: flex;
    flex-direction: column;
    align-items: center;
    gap: 20px;
  }
  .back-brand .brand-square {
    width: 210px;
    height: 210px;
  }
  .back-brand .brand-name {
    font-size: 34px;
  }
</style>
</head>
<body>
  <section class="card card--front" aria-label="Business card front">
    <div class="brand">
      <div class="brand-square" aria-hidden="true"></div>
      <div class="brand-name">Brovenna</div>
    </div>
    <div class="name-band">
      <div class="person-name">Marcus T. Hollenbrand</div>
      <div class="person-title">CEO</div>
    </div>
    <div class="contact-line">
      <span>www.brovennatrading.example</span>
      <span class="sep">•</span>
      <span>mark@brovennatrading.example</span>
      <span class="sep">•</span>
      <span>P 555-294-6172</span>
    </div>
  </section>

  <section class="card card--back" aria-label="Business card back">
    <div class="back-brand">
      <div class="brand-square" aria-hidden="true"></div>
      <div class="brand-name">Brovenna</div>
    </div>
  </section>
</body>
</html>
```